Business Card Design For A Renovation Contractor Company

We need a business card for a new company based in Singapore, our company name is "KT Planora". We are a renovation contractor that builds designs into reality. We build more of F&B restaurants, retail stores and commercial offices. We work very closely with designers. The final design should communicate to our client that we are a company that you can trust, that will plan and complete your project without giving you a headache. I like my client to remember my company as "KT". The beauty of SIMPLE is important.

Industry/Entity Type

Contractor

Requirements
Nice to have
• Black or Red base

```html
<!DOCTYPE html>
<html lang="en">
<head>
<meta charset="utf-8">
<title>KT Planora – Business Card</title>
<link rel="stylesheet" href="https://fonts.googleapis.com/css2?family=Open+Sans:wght@400;600;700&display=swap">
<style>
  :root {
    --backdrop: #e4e2de;
    --card-black: #151618;
    --band-black: #0f1011;
    --name-box: #1c1d1f;
    --brand-red: #d0141b;
    --tag-red: #b8262a;
    --title-violet: #a878b4;
    --ink-white: #f2f2f2;
    --rule: #2a2b2e;
  }
  * { box-sizing: border-box; margin: 0; padding: 0; }
  html, body { width: 1200px; height: 1000px; overflow: hidden; }
  body {
    background: var(--backdrop);
    font-family: "Open Sans", sans-serif;
    position: relative;
  }
  .card {
    position: absolute;
    top: 345px;
    width: 540px;
    height: 310px;
    background: var(--card-black);
    box-shadow: 0 10px 24px rgba(0,0,0,.25);
    overflow: hidden;
  }
  .card--front { left: 40px; }
  .card--back { left: 620px; }

  /* Front */
  .front-mark {
    position: absolute;
    inset: 0;
    display: flex;
    align-items: center;
    justify-content: center;
    gap: 16px;
  }
  .front-mark__dot {
    width: 22px; height: 22px; border-radius: 50%;
    background: var(--brand-red);
  }
  .front-mark__name {
    color: var(--brand-red);
    font-weight: 600;
    font-size: 46px;
    letter-spacing: 1px;
  }

  /* Back */
  .brand {
    position: absolute;
    left: 130px;
    top: 70px;
    width: 210px;
    text-align: center;
  }
  .brand__name {
    color: var(--brand-red);
    font-weight: 600;
    font-size: 32px;
    line-height: 1;
    white-space: nowrap;
  }
  .brand__tagline {
    margin-top: 10px;
    color: var(--tag-red);
    font-size: 11px;
    letter-spacing: .3px;
    white-space: nowrap;
  }
  .contacts {
    position: absolute;
    right: 26px;
    top: 34px;
    list-style: none;
    color: var(--ink-white);
    font-size: 12px;
  }
  .contacts__item {
    display: flex;
    align-items: center;
    gap: 10px;
    height: 24px;
    white-space: nowrap;
  }
  .contacts__icon { width: 16px; height: 14px; fill: var(--ink-white); flex: none; }
  .bottom-band {
    position: absolute;
    left: 0; right: 0; bottom: 0;
    height: 86px;
    background: var(--band-black);
    border-top: 1px solid var(--rule);
  }
  .person {
    position: absolute;
    left: 18px;
    bottom: 14px;
    width: 230px;
    height: 58px;
    background: var(--name-box);
    display: flex;
    align-items: center;
    gap: 12px;
    padding-left: 14px;
  }
  .person__marker {
    width: 20px; height: 20px; border-radius: 50%;
    background: var(--brand-red);
    flex: none;
  }
  .person__name {
    color: var(--ink-white);
    font-weight: 700;
    font-size: 15px;
    line-height: 1.2;
  }
  .person__title {
    color: var(--title-violet);
    font-size: 15px;
    line-height: 1.2;
  }
</style>
</head>
<body>

  <section class="card card--front" aria-label="Card front">
    <div class="front-mark">
      <span class="front-mark__dot"></span>
      <span class="front-mark__name">KT Planora</span>
    </div>
  </section>

  <section class="card card--back" aria-label="Card back">
    <div class="brand">
      <div class="brand__name">KT Planora</div>
      <div class="brand__tagline">spaces planned, built right</div>
    </div>

    <ul class="contacts">
      <li class="contacts__item">
        <svg class="contacts__icon" viewBox="0 0 16 12"><path d="M0 0h16v12H0z M1.5 1.5L8 7l6.5-5.5" fill="var(--ink-white)" stroke="var(--card-black)" stroke-width="1.2"/></svg>
        dtan@ktplanora.com
      </li>
      <li class="contacts__item">
        <svg class="contacts__icon" viewBox="0 0 16 14"><rect x="4.5" y="0.5" width="7" height="13" rx="1.2" fill="none" stroke="var(--ink-white)"/><circle cx="8" cy="11.5" r=".8"/></svg>
        0198 23451 907
      </li>
      <li class="contacts__item">
        <svg class="contacts__icon" viewBox="0 0 16 14"><circle cx="8" cy="7" r="6.5" fill="none" stroke="var(--ink-white)"/><ellipse cx="8" cy="7" rx="2.8" ry="6.5" fill="none" stroke="var(--ink-white)"/><path d="M1.5 7h13" stroke="var(--ink-white)"/></svg>
        www.ktplanora.com
      </li>
    </ul>

    <div class="bottom-band"></div>

    <div class="person">
      <span class="person__marker"></span>
      <div>
        <div class="person__name">Daniel Tan</div>
        <div class="person__title">Senior Manager</div>
      </div>
    </div>
  </section>

</body>
</html>
```